AV & Engineering company needs a Business Card Design

Like the simple design, don't too colorful. Smart & professional feel

Industry/Entity Type

Business

Requirements
Nice to have
• I would like to see the vertical design.

```html
<!DOCTYPE html>
<html lang="en">
<head>
<meta charset="utf-8">
<title>Norvane Systems – Business Card</title>
<link rel="stylesheet" href="https://fonts.googleapis.com/css2?family=Open+Sans:wght@400;600;700&display=swap">
<style>
  :root {
    --backdrop: #3b322e;
    --card: #fbfbfb;
    --brand-red: #9b1b22;
    --ink: #2f2f2f;
    --muted: #555555;
  }
  * { box-sizing: border-box; margin: 0; padding: 0; }
  html, body {
    width: 1200px;
    height: 768px;
    overflow: hidden;
    background: var(--backdrop);
    font-family: "Open Sans", Arial, sans-serif;
  }
  .stage {
    position: relative;
    width: 1200px;
    height: 768px;
  }
  .card {
    position: absolute;
    top: 229px;
    width: 540px;
    height: 310px;
    background: var(--card);
    box-shadow: 0 10px 26px rgba(0,0,0,.35);
  }
  .card--front { left: 45px; }
  .card--back  { left: 615px; }

  .wordmark {
    display: flex;
    align-items: center;
    gap: 14px;
    color: var(--brand-red);
    font-weight: 700;
    text-transform: uppercase;
    line-height: 1.05;
  }
  .wordmark__square {
    flex: none;
    background: var(--brand-red);
  }
  .card--front .wordmark {
    position: absolute;
    left: 70px;
    top: 112px;
    font-size: 30px;
    letter-spacing: .5px;
  }
  .card--front .wordmark__square { width: 56px; height: 56px; }
  .card--front .wordmark__sub { font-size: 22px; letter-spacing: 3px; }

  .card--back .wordmark {
    position: absolute;
    right: 30px;
    top: 118px;
    font-size: 17px;
    gap: 9px;
  }
  .card--back .wordmark__square { width: 32px; height: 32px; }
  .card--back .wordmark__sub { font-size: 13px; letter-spacing: 2px; }

  .holder {
    position: absolute;
    left: 34px;
    top: 36px;
  }
  .holder__name {
    color: var(--brand-red);
    font-weight: 700;
    font-size: 15px;
  }
  .holder__role {
    color: var(--muted);
    font-size: 10px;
    margin-top: 1px;
  }

  .contacts {
    position: absolute;
    left: 34px;
    bottom: 40px;
    list-style: none;
    color: var(--ink);
    font-size: 12.5px;
  }
  .contacts li {
    display: flex;
    align-items: center;
    gap: 8px;
    height: 20px;
  }
  .contacts .pair { gap: 8px; }
  .contacts .pair span + svg { margin-left: 8px; }
  .icon { width: 11px; height: 11px; fill: var(--brand-red); flex: none; }
  .accent { color: var(--brand-red); }
</style>
</head>
<body>
<main class="stage">

  <section class="card card--front" aria-label="Business card front">
    <div class="wordmark">
      <span class="wordmark__square"></span>
      <span>Norvane Systems<br><span class="wordmark__sub">Company Ltd</span></span>
    </div>
  </section>

  <section class="card card--back" aria-label="Business card back">
    <div class="holder">
      <p class="holder__name">Your Long Name</p>
      <p class="holder__role">Managing Director</p>
    </div>

    <div class="wordmark">
      <span class="wordmark__square"></span>
      <span>Norvane Systems<br><span class="wordmark__sub">Company Ltd</span></span>
    </div>

    <ul class="contacts">
      <li>
        <svg class="icon" viewBox="0 0 12 12"><path d="M6 0a4 4 0 0 0-4 4c0 3 4 8 4 8s4-5 4-8a4 4 0 0 0-4-4zm0 5.6A1.6 1.6 0 1 1 6 2.4a1.6 1.6 0 0 1 0 3.2z"/></svg>
        <span>Your Commercial or office address</span>
      </li>
      <li class="pair">
        <svg class="icon" viewBox="0 0 12 12"><path d="M2.4 0.5l2 2.2-1 1.4a7 7 0 0 0 4.5 4.5l1.4-1 2.2 2-1.3 1.9C5 11.3 0.7 7 0.5 1.8z"/></svg>
        <span>00.00.00.0000</span>
        <svg class="icon" viewBox="0 0 12 12"><path d="M3 0h6v3H3zM1 4h10v6H1zM3 8h6v4H3z"/></svg>
        <span>00.00.00.0000</span>
      </li>
      <li>
        <svg class="icon" viewBox="0 0 12 12"><path d="M0 2h12v8H0zM1 3l5 4 5-4" stroke="#fbfbfb" stroke-width="1"/></svg>
        <span>yourname@yourwebsite.com</span>
      </li>
      <li>
        <svg class="icon" viewBox="0 0 12 12"><circle cx="6" cy="6" r="5.5"/><path d="M0.5 6h11M6 0.5c-3 3-3 8 0 11M6 0.5c3 3 3 8 0 11" stroke="#fbfbfb" stroke-width=".8" fill="none"/></svg>
        <span>www.<span class="accent">yourwebsite</span>.com</span>
      </li>
    </ul>
  </section>

</main>
</body>
</html>
```